Software Architecture Drawing

I have a software architecture that we would like to pretty up. Our current drawing was done in VISIO, but it just doesn't look professional (and salesy) enough. We would like an illustration that is attractive, makes simple use of colour, and allows us to make little tweaks (wording, etc.). We used icons for certain concepts, but these will have to be redrawn (or purchased). This particular software application is able to receive many data points, store it in a high performance data store, and make it available to various users for analysis or other systems for other purposes

Target Market(s)

Software Architects, IT Professionals

Industry/Entity Type

Software

Font styles to use
Sans Serif

Colors
0355a3
3176b5
85acd3
cedeec
f37022
f68e4e

Requirements
Must have
• Unique (or legal copies) of logos to represent various input sources.

```html
<!DOCTYPE html>
<html lang="en">
<head>
<meta charset="utf-8">
<title>Software Architecture</title>
<link href="https://fonts.googleapis.com/css2?family=Source+Sans+3:wght@400;600;700;900&display=swap" rel="stylesheet">
<style>
  :root{
    --navy:#0355a3;
    --mid:#3176b5;
    --soft:#85acd3;
    --pale:#cedeec;
    --white:#ffffff;
    --ink:#000000;
    --edge:#17406e;
  }
  *{box-sizing:border-box;margin:0;padding:0}
  html,body{width:1200px;height:1000px;overflow:hidden}
  body{font-family:"Source Sans 3",Arial,sans-serif;background:var(--pale);position:relative}
  .canvas{position:relative;width:1200px;height:1000px;overflow:hidden}
  .upper{position:absolute;left:0;top:0;width:1200px;height:592px;background:var(--pale)}
  .lower{position:absolute;left:0;top:592px;width:1200px;height:408px;background:var(--soft)}

  .sources-title{position:absolute;left:46px;top:0;font-size:15px;font-weight:700;color:var(--navy)}
  .source{position:absolute;left:22px;width:134px;background:var(--mid);border-radius:7px;color:var(--white);font-size:15px;line-height:1.15}
  .source .icon{position:absolute;left:7px;top:50%;transform:translateY(-50%);width:42px;height:42px;border-radius:4px;background:linear-gradient(135deg,#1b3f6a,#4f86bf)}
  .source .label{position:absolute;right:6px;text-align:center}

  .column{position:absolute;background:var(--mid);border-radius:4px;color:var(--white);display:flex;align-items:center;justify-content:center}
  .vertical{writing-mode:vertical-rl;transform:rotate(180deg);text-align:center;white-space:nowrap}
  .ingest{left:276px;top:25px;width:76px;height:543px;font-size:36px}
  .framework{left:459px;top:25px;width:219px;height:543px;border:1px solid var(--edge);justify-content:flex-start;align-items:stretch}
  .framework .name{width:89px;font-size:27px;line-height:1.1;display:flex;align-items:center;justify-content:center;padding-left:6px}
  .framework .name span{display:block}
  .utility{position:absolute;left:88px;top:-1px;width:130px;height:470px;border:1px solid var(--edge);border-radius:4px;background:var(--mid);display:flex;align-items:center;justify-content:center;padding-top:62px;font-size:29px;line-height:1.15}
  .viz{left:793px;top:191px;width:75px;height:377px;font-size:26px}

  .output{position:absolute;left:998px;width:177px;height:116px;background:var(--mid);border-radius:7px;overflow:hidden}
  .unknown{left:992px;top:28px;height:116px;display:flex;align-items:center;justify-content:center;font-size:108px;font-weight:900;color:var(--ink)}
  .map-area{position:absolute;left:10px;top:22px;width:157px;height:76px;border-radius:6px;background:linear-gradient(180deg,#2a5f97,#4d86c0)}

  .services{position:absolute;left:242px;top:686px;width:660px;height:64px;background:var(--pale);border-radius:8px;color:var(--mid);font-size:50px;text-align:center;line-height:60px;padding-left:18px}
  .client{position:absolute;top:883px;width:222px;height:102px;background:var(--pale);border-radius:8px;color:var(--mid);font-size:24px;font-weight:700;line-height:1.25;display:flex;align-items:center;justify-content:center;text-align:center;padding-bottom:8px}

  .arrows{position:absolute;left:0;top:0;width:1200px;height:1000px;pointer-events:none}
  .arrows use{fill:var(--navy)}
</style>
</head>
<body>
<div class="canvas">
  <div class="upper"></div>
  <div class="lower"></div>

  <div class="sources-title">Data Sources</div>

  <div class="source" style="top:26px;height:62px"><div class="icon" role="img" aria-label="Starburst icon for special data"></div><div class="label" style="right:22px;bottom:10px">Special</div></div>
  <div class="source" style="top:102px;height:56px"><div class="icon" role="img" aria-label="Gear icon for operational data"></div><div class="label" style="bottom:12px">Operational</div></div>
  <div class="source" style="top:178px;height:62px"><div class="icon" role="img" aria-label="Network icon for enterprise data"></div><div class="label" style="bottom:24px">Enterprise</div></div>
  <div class="source" style="top:246px;height:62px"><div class="icon" role="img" aria-label="People icon for customer data"></div><div class="label" style="right:10px;bottom:7px">Customer</div></div>
  <div class="source" style="top:317px;height:54px"><div class="icon" role="img" aria-label="House icon for property data"></div><div class="label" style="right:17px;bottom:6px">Property</div></div>
  <div class="source" style="top:383px;height:54px"><div class="icon" role="img" aria-label="Globe icon for geospatial data"></div><div class="label" style="bottom:6px">Geospatial</div></div>
  <div class="source" style="top:448px;height:56px"><div class="icon" role="img" aria-label="Social network icon"></div><div class="label" style="right:18px;bottom:6px">Social<br>Media</div></div>
  <div class="source" style="top:518px;height:50px"><div class="icon" role="img" aria-label="Sun and cloud icon for weather data"></div><div class="label" style="right:13px;bottom:9px">Weather</div></div>

  <div class="column ingest"><div class="vertical">Some Text About Here</div></div>

  <div class="column framework">
    <div class="name"><div class="vertical"><span>Quorvel Low-Latency</span><span>Transaction Execution Framework</span></div></div>
    <div class="utility"><div class="vertical">High-Performance<br>Sensational<br>Utility</div></div>
  </div>

  <div class="column viz"><div class="vertical">All sorts of Visualization Tools</div></div>

  <div class="output unknown">?</div>

  <div class="output" style="top:181px">
    <svg width="177" height="116" viewBox="0 0 177 116">
      <polyline points="17,10 17,97 156,97" fill="none" stroke="var(--ink)" stroke-width="5"/>
      <polyline points="19,95 40,62 56,76 81,27 93,61 132,31" fill="none" stroke="var(--white)" stroke-width="2.5"/>
    </svg>
  </div>

  <div class="output" style="top:308px">
    <div class="map-area" role="img" aria-label="Map with location pins"></div>
  </div>

  <div class="output" style="top:436px">
    <svg width="177" height="116" viewBox="0 0 177 116">
      <rect x="14" y="16" width="145" height="84" fill="var(--mid)" stroke="var(--ink)" stroke-width="3"/>
      <rect x="14" y="16" width="16" height="84" fill="var(--ink)"/>
      <rect x="14" y="16" width="145" height="10" fill="var(--ink)"/>
      <g stroke="var(--white)" stroke-width="2">
        <line x1="30" y1="45" x2="158" y2="45"/><line x1="30" y1="64" x2="158" y2="64"/><line x1="30" y1="82" x2="158" y2="82"/>
        <line x1="52" y1="26" x2="52" y2="99"/><line x1="77" y1="26" x2="77" y2="99"/><line x1="100" y1="26" x2="100" y2="99"/><line x1="122" y1="26" x2="122" y2="99"/><line x1="142" y1="26" x2="142" y2="99"/>
      </g>
    </svg>
  </div>

  <div class="services">Web Services</div>

  <div class="client" style="left:179px">Customer<br>Presentment</div>
  <div class="client" style="left:448px">Conservation<br>Idea</div>
  <div class="client" style="left:710px">Custom<br>Clients</div>

  <svg class="arrows" viewBox="0 0 1200 1000" aria-hidden="true">
    <defs>
      <symbol id="arrow-right" viewBox="0 0 80 40" preserveAspectRatio="none"><path d="M0 11H48V0L80 20L48 40V29H0Z"/></symbol>
      <symbol id="arrow-both" viewBox="0 0 80 40" preserveAspectRatio="none"><path d="M0 20L24 0V11H56V0L80 20L56 40V29H24V40Z"/></symbol>
      <symbol id="arrow-down" viewBox="0 0 40 80" preserveAspectRatio="none"><path d="M11 0H29V48H40L20 80L0 48H11Z"/></symbol>
    </defs>
    <use href="#arrow-right" x="180" y="38" width="78" height="40"/>
    <use href="#arrow-both" x="174" y="110" width="84" height="38"/>
    <use href="#arrow-both" x="176" y="188" width="84" height="38"/>
    <use href="#arrow-both" x="176" y="260" width="84" height="38"/>
    <use href="#arrow-both" x="172" y="326" width="84" height="38"/>
    <use href="#arrow-right" x="180" y="389" width="78" height="40"/>
    <use href="#arrow-right" x="180" y="458" width="78" height="40"/>
    <use href="#arrow-right" x="180" y="527" width="78" height="40"/>

    <use href="#arrow-both" x="364" y="108" width="82" height="38"/>
    <use href="#arrow-both" x="364" y="391" width="82" height="38"/>

    <use href="#arrow-right" x="783" y="64" width="112" height="46"/>
    <use href="#arrow-both" x="694" y="228" width="83" height="38"/>
    <use href="#arrow-both" x="694" y="391" width="83" height="38"/>

    <use href="#arrow-right" x="890" y="227" width="77" height="40"/>
    <use href="#arrow-right" x="890" y="354" width="77" height="40"/>
    <use href="#arrow-right" x="890" y="480" width="77" height="40"/>

    <use href="#arrow-down" x="538" y="592" width="42" height="74"/>
    <use href="#arrow-down" x="268" y="780" width="44" height="76"/>
    <use href="#arrow-down" x="544" y="780" width="44" height="76"/>
    <use href="#arrow-down" x="800" y="780" width="44" height="76"/>
  </svg>
</div>
</body>
</html>
```